Design a large parking banner – mandatory ticket validation in the shop

Banner Size:
548 cm (width) x 154 cm (height)
Note: The banner will be placed in a metal frame at our parking lot entrance, fully visible to every incoming truck driver. The message must be easy to read from a distance.
Goal of the Banner:
To inform all truck drivers that they must validate their entry ticket inside the shop, even if they are parking for a short time.
The message must be displayed in multiple languages for international drivers.
Mandatory Content:
Main message – in multiple languages (clearly separated or stacked):
Dutch (NL): Vergeet je ticket niet te valideren in de shop – verplicht, ook bij kort parkeren!
French (FR): N'oubliez pas de valider votre ticket à la boutique – obligatoire, même pour un court arrêt !
English (EN): Don't forget to validate your entry ticket in the shop – mandatory, even for short stops!
German (DE): Vergessen Sie nicht, Ihr Einfahrticket im Shop zu entwerten – Pflicht, auch bei kurzem Parken!
Polish (PL): Nie zapomnij zatwierdzić biletu w sklepie – obowiązkowe, nawet przy krótkim postoju!
Romanian (RO): Nu uitați să validați biletul în magazin – obligatoriu, chiar și pentru opriri scurte!
You can include more languages if space allows, but these are essential.
Opening Hours Block (in one section below):
Shop Opening Hours
Mon – Fri: 05:30 – 22:00
Sat & Sun: 08:00 – 22:00
Style & Branding:
The design must match the visual identity of Haulport 41Ter
Please refer to the attached photos of existing parking signage for guidance on colors, typography, and layout style
Our logo (attached) must be clearly visible and professionally integrated
Feel free to use icons or pictograms to visually support the message (e.g., ticket, truck, arrow)
Readability is key – large, bold text and high contrast colors that are visible from a distance
Target Audience:
International truck drivers – people who need fast, clear communication. Not everyone speaks the local language, so visual clarity and multilingual messaging are critical.
File Requirements:
Print-ready file (PDF or EPS) – 300 dpi at 1:10 scale
Include 5 cm bleed on all sides
Provide open source files if possible (AI or PSD)

```html
<!DOCTYPE html>
<html lang="en">
<head>
<meta charset="utf-8">
<title>Haulport 41Ter – Ticket Validation Banner</title>
<link rel="stylesheet" href="https://fonts.googleapis.com/css2?family=Source+Sans+3:wght@600;700&family=Open+Sans:wght@300;400;600&display=swap">
<style>
  :root {
    --page: #ffffff;
    --navy: #2e2d86;
    --navy-deep: #272a6c;
    --navy-light: #3a3aa8;
    --ink: #111111;
    --white: #ffffff;
    --red: #e3262b;
    --blue: #1e88d0;
    --silver-dark: #a9abae;
    --silver-light: #f2f2f2;
    --rule-silver: #9a9c9f;
  }
  * { box-sizing: border-box; margin: 0; padding: 0; }
  html, body { width: 782px; height: 1200px; overflow: hidden; background: var(--page); }
  .sheet { position: relative; width: 782px; height: 1200px; }

  .banner {
    position: absolute; left: 66px; width: 639px; height: 180px; overflow: hidden;
    font-family: "Source Sans 3", sans-serif;
  }
  .banner--hero { top: 146px; }
  .banner--blue-a { top: 527px; }
  .banner--silver-round { top: 738px; border-radius: 18px; }
  .banner--silver-navy { top: 951px; }

  .banner--blue { background: radial-gradient(ellipse at 40% 70%, var(--navy-light), var(--navy) 60%); color: var(--white); }
  .banner--silver {
    background: linear-gradient(100deg, var(--silver-dark) 0%, var(--silver-light) 22%, #b4b6b9 40%, var(--silver-light) 58%, #a8aaad 78%, #e6e6e6 100%);
    color: var(--ink);
  }

  .brand {
    position: absolute; left: 14px; top: 30px; width: 118px;
    text-align: center; font-weight: 700; font-size: 17px; line-height: 1.05;
  }
  .banner--blue .brand { color: var(--white); }
  .banner--silver .brand { color: var(--navy-deep); }

  .ticket-icon { position: absolute; left: 48px; top: 83px; width: 48px; height: 48px; }
  .ticket-icon * { fill: none; stroke-width: 2; }
  .banner--blue .ticket-icon * { stroke: var(--white); }
  .banner--silver-round .ticket-icon * { stroke: var(--ink); }
  .banner--silver-navy .ticket-icon * { stroke: var(--navy-deep); }

  .messages { position: absolute; left: 150px; top: 18px; width: 467px; list-style: none; }
  .message {
    display: flex; align-items: center; height: 20px; white-space: nowrap;
    font-weight: 600; font-size: 10.2px; letter-spacing: -0.1px;
    border-bottom: 0.6px solid var(--red);
  }
  .message:last-child { border-bottom: none; }
  .banner--silver .message { border-bottom-color: var(--rule-silver); }
  .banner--silver .message:last-child { border-bottom: none; }
  .lang { width: 16px; }
  .lang-mark { width: 7px; height: 7px; background: var(--red); margin-right: 14px; }
  .banner--silver-navy .lang-mark { background: var(--blue); }

  .hours {
    position: absolute; left: 0; right: 0; bottom: 0; height: 27px;
    display: flex; align-items: center; padding-left: 150px;
    font-family: "Open Sans", sans-serif; font-size: 10.5px; color: var(--white);
    background: var(--ink);
  }
  .banner--silver-navy .hours { background: var(--navy-deep); }
  .hours-label { font-weight: 300; width: 122px; }
  .banner--blue .hours-label { color: var(--red); }
  .hours-time { font-weight: 600; letter-spacing: 0.2px; }
  .hours-divider { margin: 0 10px; font-weight: 400; }
  .banner--blue .hours-divider { color: var(--red); }
</style>
</head>
<body>
<div class="sheet">

  <!-- Banner template repeated in four colourways -->
  <section class="banner banner--blue banner--hero">
    <div class="brand">Haulport<br>41Ter</div>
    <svg class="ticket-icon" viewBox="0 0 48 48" aria-hidden="true"><circle cx="24" cy="24" r="22"/><g transform="rotate(-40 24 24)"><rect x="12" y="17" width="24" height="14" rx="2"/><line x1="29" y1="17" x2="29" y2="31" stroke-dasharray="2 2"/></g></svg>
    <ul class="messages">
      <li class="message"><span class="lang">NL</span><span class="lang-mark"></span>Vergeet je ticket niet te valideren in de shop – verplicht, ook bij kort parkeren!</li>
      <li class="message"><span class="lang">FR</span><span class="lang-mark"></span>N'oubliez pas de valider votre ticket à la boutique – obligatoire, même pour un court arrêt !</li>
      <li class="message"><span class="lang">EN</span><span class="lang-mark"></span>Don't forget to validate your entry ticket in the shop – mandatory, even for short stops!</li>
      <li class="message"><span class="lang">DE</span><span class="lang-mark"></span>Vergessen Sie nicht, Ihr Einfahrticket im Shop zu entwerten – Pflicht, auch bei kurzem Parken!</li>
      <li class="message"><span class="lang">PL</span><span class="lang-mark"></span>Nie zapomnij zatwierdzić biletu w sklepie – obowiązkowe, nawet przy krótkim postoju!</li>
      <li class="message"><span class="lang">RO</span><span class="lang-mark"></span>Nu uitați să validați biletul în magazin – obligatoriu, chiar și pentru opriri scurte!</li>
    </ul>
    <div class="hours"><span class="hours-label">Shop Opening Hours:</span><span class="hours-time">Mon-Fri : 05:30 - 22:00</span><span class="hours-divider">I</span><span class="hours-time">Sat &amp; Sun : 08:00 - 22:00</span></div>
  </section>

  <section class="banner banner--blue banner--blue-a">
    <div class="brand">Haulport<br>41Ter</div>
    <svg class="ticket-icon" viewBox="0 0 48 48" aria-hidden="true"><circle cx="24" cy="24" r="22"/><g transform="rotate(-40 24 24)"><rect x="12" y="17" width="24" height="14" rx="2"/><line x1="29" y1="17" x2="29" y2="31" stroke-dasharray="2 2"/></g></svg>
    <ul class="messages">
      <li class="message"><span class="lang">NL</span><span class="lang-mark"></span>Vergeet je ticket niet te valideren in de shop – verplicht, ook bij kort parkeren!</li>
      <li class="message"><span class="lang">FR</span><span class="lang-mark"></span>N'oubliez pas de valider votre ticket à la boutique – obligatoire, même pour un court arrêt !</li>
      <li class="message"><span class="lang">EN</span><span class="lang-mark"></span>Don't forget to validate your entry ticket in the shop – mandatory, even for short stops!</li>
      <li class="message"><span class="lang">DE</span><span class="lang-mark"></span>Vergessen Sie nicht, Ihr Einfahrticket im Shop zu entwerten – Pflicht, auch bei kurzem Parken!</li>
      <li class="message"><span class="lang">PL</span><span class="lang-mark"></span>Nie zapomnij zatwierdzić biletu w sklepie – obowiązkowe, nawet przy krótkim postoju!</li>
      <li class="message"><span class="lang">RO</span><span class="lang-mark"></span>Nu uitați să validați biletul în magazin – obligatoriu, chiar și pentru opriri scurte!</li>
    </ul>
    <div class="hours"><span class="hours-label">Shop Opening Hours:</span><span class="hours-time">Mon-Fri : 05:30 - 22:00</span><span class="hours-divider">I</span><span class="hours-time">Sat &amp; Sun : 08:00 - 22:00</span></div>
  </section>

  <section class="banner banner--silver banner--silver-round">
    <div class="brand">Haulport<br>41Ter</div>
    <svg class="ticket-icon" viewBox="0 0 48 48" aria-hidden="true"><circle cx="24" cy="24" r="22"/><g transform="rotate(-40 24 24)"><rect x="12" y="17" width="24" height="14" rx="2"/><line x1="29" y1="17" x2="29" y2="31" stroke-dasharray="2 2"/></g></svg>
    <ul class="messages">
      <li class="message"><span class="lang">NL</span><span class="lang-mark"></span>Vergeet je ticket niet te valideren in de shop – verplicht, ook bij kort parkeren!</li>
      <li class="message"><span class="lang">FR</span><span class="lang-mark"></span>N'oubliez pas de valider votre ticket à la boutique – obligatoire, même pour un court arrêt !</li>
      <li class="message"><span class="lang">EN</span><span class="lang-mark"></span>Don't forget to validate your entry ticket in the shop – mandatory, even for short stops!</li>
      <li class="message"><span class="lang">DE</span><span class="lang-mark"></span>Vergessen Sie nicht, Ihr Einfahrticket im Shop zu entwerten – Pflicht, auch bei kurzem Parken!</li>
      <li class="message"><span class="lang">PL</span><span class="lang-mark"></span>Nie zapomnij zatwierdzić biletu w sklepie – obowiązkowe, nawet przy krótkim postoju!</li>
      <li class="message"><span class="lang">RO</span><span class="lang-mark"></span>Nu uitați să validați biletul în magazin – obligatoriu, chiar și pentru opriri scurte!</li>
    </ul>
    <div class="hours"><span class="hours-label">Shop Opening Hours:</span><span class="hours-time">Mon-Fri : 05:30 - 22:00</span><span class="hours-divider">I</span><span class="hours-time">Sat &amp; Sun : 08:00 - 22:00</span></div>
  </section>

  <section class="banner banner--silver banner--silver-navy">
    <div class="brand">Haulport<br>41Ter</div>
    <svg class="ticket-icon" viewBox="0 0 48 48" aria-hidden="true"><circle cx="24" cy="24" r="22"/><g transform="rotate(-40 24 24)"><rect x="12" y="17" width="24" height="14" rx="2"/><line x1="29" y1="17" x2="29" y2="31" stroke-dasharray="2 2"/></g></svg>
    <ul class="messages">
      <li class="message"><span class="lang">NL</span><span class="lang-mark"></span>Vergeet je ticket niet te valideren in de shop – verplicht, ook bij kort parkeren!</li>
      <li class="message"><span class="lang">FR</span><span class="lang-mark"></span>N'oubliez pas de valider votre ticket à la boutique – obligatoire, même pour un court arrêt !</li>
      <li class="message"><span class="lang">EN</span><span class="lang-mark"></span>Don't forget to validate your entry ticket in the shop – mandatory, even for short stops!</li>
      <li class="message"><span class="lang">DE</span><span class="lang-mark"></span>Vergessen Sie nicht, Ihr Einfahrticket im Shop zu entwerten – Pflicht, auch bei kurzem Parken!</li>
      <li class="message"><span class="lang">PL</span><span class="lang-mark"></span>Nie zapomnij zatwierdzić biletu w sklepie – obowiązkowe, nawet przy krótkim postoju!</li>
      <li class="message"><span class="lang">RO</span><span class="lang-mark"></span>Nu uitați să validați biletul în magazin – obligatoriu, chiar și pentru opriri scurte!</li>
    </ul>
    <div class="hours"><span class="hours-label">Shop Opening Hours:</span><span class="hours-time">Mon-Fri : 05:30 - 22:00</span><span class="hours-divider">I</span><span class="hours-time">Sat &amp; Sun : 08:00 - 22:00</span></div>
  </section>

</div>
</body>
</html>
```